Business Card Design

Extremely classy understated design.

Printing in fancy scrip or hand writing.

Conservative color scheme such as black print on beige paper. I am sure you have much better ideas than I would have.

I am involved in a number of different businesses and require a simple elegant business card.

I would like a object on the card, such as, a bald eagle, an antique Ashcombe Vance, a water fall or a beautiful flower.
Updates

My name is: Leon T. Marsh Not Leon T. Marsh Investments Investments is my occupation Most of the designs are not acceptable. Very disappointed with results.

Industry/Entity Type

Business

Contact Information for Business Card

Leon T Marsh
Investments
555 614 2790
kestrellm@postvale.net

```html
<!DOCTYPE html>
<html lang="en">
<head>
<meta charset="utf-8">
<title>Leon T Marsh – Business Card</title>
<link rel="stylesheet" href="https://fonts.googleapis.com/css2?family=Open+Sans:wght@400&family=Pinyon+Script&display=swap">
<style>
  :root {
    --page-bg: #f4f4f4;
    --card-black: #0b0b0b;
    --pattern-light: #262626;
    --pattern-dark: #080808;
    --band-black: #030303;
    --gold: #c9a13a;
    --gold-light: #f0d27a;
    --gold-dark: #8a6a1c;
    --silver: #d6d6d6;
    --text-light: #e8e8e8;
  }
  * { box-sizing: border-box; margin: 0; padding: 0; }
  html, body {
    width: 1200px;
    height: 900px;
    overflow: hidden;
    background: var(--page-bg);
  }
  .canvas {
    position: relative;
    width: 1200px;
    height: 900px;
  }
  .card {
    position: absolute;
    top: 295px;
    width: 510px;
    height: 310px;
    border-radius: 24px;
    overflow: hidden;
    background: var(--card-black);
  }
  .card--back { left: 60px; }
  .card--front { left: 630px; }

  .card__pattern {
    position: absolute;
    inset: 0;
    background: radial-gradient(ellipse at 50% 40%, var(--pattern-light) 0%, #161616 45%, var(--pattern-dark) 100%);
  }

  .card__band {
    position: absolute;
    left: 0;
    right: 0;
    top: 108px;
    height: 56px;
    background: var(--band-black);
    border-top: 2px solid var(--gold);
    border-bottom: 2px solid var(--gold);
  }

  .contact {
    position: absolute;
    left: 135px;
    top: 113px;
    font-family: "Open Sans", sans-serif;
    font-size: 17px;
    line-height: 23px;
    color: var(--text-light);
    list-style: none;
  }
  .contact__item {
    display: flex;
    align-items: center;
    gap: 7px;
  }
  .contact__icon {
    width: 16px;
    height: 16px;
    flex: none;
  }

  .ornament {
    position: absolute;
    left: 176px;
    width: 180px;
    border-radius: 40%;
    background: radial-gradient(ellipse at 50% 50%, var(--gold-light) 0%, var(--gold) 40%, rgba(138,106,28,0) 75%);
  }
  .ornament--top { top: 42px; height: 70px; }
  .ornament--bottom { top: 162px; height: 78px; }

  .identity {
    position: absolute;
    left: 0;
    right: 0;
    top: 110px;
    height: 54px;
    text-align: center;
    padding-left: 30px;
  }
  .identity__name {
    font-family: "Pinyon Script", cursive;
    font-size: 40px;
    line-height: 40px;
    color: var(--silver);
    font-weight: 400;
  }
  .identity__occupation {
    font-family: "Open Sans", sans-serif;
    font-size: 11px;
    letter-spacing: 4px;
    color: var(--silver);
    line-height: 12px;
  }
</style>
</head>
<body>
<main class="canvas">

  <section class="card card--back" aria-label="Card back">
    <div class="card__pattern" role="img" aria-label="Dark black damask floral pattern"></div>
    <div class="card__band"></div>
    <ul class="contact">
      <li class="contact__item">
        <svg class="contact__icon" viewBox="0 0 24 24" aria-hidden="true">
          <path fill="var(--gold)" d="M6.6 10.8a15.1 15.1 0 0 0 6.6 6.6l2.2-2.2a1 1 0 0 1 1-.25 11.4 11.4 0 0 0 3.6.57 1 1 0 0 1 1 1V20a1 1 0 0 1-1 1A17 17 0 0 1 3 4a1 1 0 0 1 1-1h3.5a1 1 0 0 1 1 1c0 1.25.2 2.45.57 3.57a1 1 0 0 1-.25 1z"/>
        </svg>
        <span>555 614 2790</span>
      </li>
      <li class="contact__item">
        <svg class="contact__icon" viewBox="0 0 24 24" aria-hidden="true">
          <rect x="2" y="5" width="20" height="14" rx="1.5" fill="var(--gold)"/>
          <path d="M3 6.5l9 6.5 9-6.5" fill="none" stroke="var(--band-black)" stroke-width="1.6"/>
        </svg>
        <span>kestrellm@postvale.net</span>
      </li>
    </ul>
  </section>

  <section class="card card--front" aria-label="Card front">
    <div class="card__pattern" role="img" aria-label="Dark black damask floral pattern"></div>
    <div class="card__band"></div>
    <div class="ornament ornament--top" role="img" aria-label="Gold baroque scroll ornament above the name"></div>
    <div class="ornament ornament--bottom" role="img" aria-label="Gold baroque scroll ornament below the name"></div>
    <div class="identity">
      <h1 class="identity__name">Leon T Marsh</h1>
      <p class="identity__occupation">Investments</p>
    </div>
  </section>

</main>
</body>
</html>
```